Web-page design

We need a initial web design for our page kelbrook.com.au (which is not yet set up).
We provide consulting services for all kinds of problems in and between organisations.
Main focus is on conflict resolution but we also support companies on improving their operational performance.
We want to have the following page structure (and part of the project is to design the 8 pages):
- Home
- Services (we offer 3 main service areas - one per page)
- Case studies (one per page)
- Engaging us (our process)
- About Conflict & low performance
- Conflict resolution App
- About
- Contact (Email form)
- Our logo should be on each page.
The start page should include the following information:
- Twitter / Linkedin / facebook/ google + Links
- Telephone / Email or in general contact details
- News
- A quite prominent picture box with 3 alternating pics - each representing one of our service areas
- Link to our App
- Testimonials
It would be nice if the service pages would have an image header. Links to the information section (about conflict & low performance; and the app page) would be nice as well.
We like the following joomla designs: www.frandelthemes.com/itempreview/153
No need to copy it, it should just give you an idea.
We like the layout here with the picture and space for the case studies on the left. Somewhere beneath should be the 3 service areas with a picture each.
In terms of colors: our logo colours are Blue (RBG 8;44;80) and Orange (RGB 231;120;23). The orange could be used to emphasise certain things, however there should not be too much color.
Budget for images available, so please use placeholders or ask us for specific photos/images, if you need them for your design.
Updates
Hi, one more thing that we would like to have is the case studies not hidden behind a link "case studies" - we would like to have them individually linked prominent on the first page. There will be about 6-8 of them. Thats what we liked on the joomla template (the links left from the picture).
Hi, thanks very much for all the great proposals.
We are currently going through the selection process and will post our decision early next week.
Thanks again!
Wilma
Target Market(s)
- target customers are all different kinds of businesses and organisations (all industries, government, non-for-profit, ...) experiencing conflict and tension - be it with internal staff, amongst managers or board members, dysfunctional teams, between organizations or customers and organizations... examples could be bullying allegations, governmental negotiations with unions, disputes within organizations etc.
- also we will offer performance improvement services for organizations
- we will offer mediation, facilitation, negotiation, performance improvement services, conflict coaching, conflict management, change management services
- if comparable to anything - then to a law firm in terms of dealing with conflicts but its much less adversarial and much more about the people and their interests rather than about laws
- basically it's all kind of things you can do in order to solve disputes without involving lawyers and a court - so it's much cheaper and target is to find a solution all parties can live with rather than having a judge deciding about who wins and who looses
- performance management is more about analysing reasons for a lack of performance and setting up continous improvement systems, supporting change management, facilitating improvement workshops or strategic meetings, ...
Industry/Entity Type
Consulting
Look and feel

```html
<!DOCTYPE html>
<html lang="en">
<head>
<meta charset="utf-8">
<title>Kelbrook – Home</title>
<link href="https://fonts.googleapis.com/css2?family=Source+Sans+3:wght@400;600&family=Arimo:ital,wght@0,400;0,700;1,400&display=swap" rel="stylesheet">
<style>
:root{
  --navy:#0b2a4c;
  --navy-deep:#082644;
  --nav-top:#1e4a78;
  --nav-bottom:#0c2d52;
  --orange:#e7781a;
  --orange-light:#f5922e;
  --text:#555a60;
  --heading:#1a3452;
  --light:#f3f3f3;
  --band:#dcdcdc;
  --white:#ffffff;
}
*{box-sizing:border-box;margin:0;padding:0}
html,body{width:1003px;height:1200px;overflow:hidden}
body{position:relative;background:var(--light);font-family:"Arimo",Arial,sans-serif;color:var(--text)}
a{color:inherit;text-decoration:none}

.site-header{position:absolute;left:0;top:0;width:1003px;height:127px;
  background:linear-gradient(#fbfbfb,#ececec)}
.brand{position:absolute;left:0;right:0;top:42px;text-align:center}
.brand-name{display:inline-flex;align-items:center;gap:12px;font-family:"Source Sans 3",sans-serif;
  font-weight:600;font-size:38px;letter-spacing:2px;color:var(--navy);line-height:1}
.brand-mark{width:18px;height:18px;background:var(--orange)}
.brand-url{position:absolute;left:0;right:0;top:97px;text-align:center;font-family:"Arimo",sans-serif;
  font-weight:700;font-size:13px;letter-spacing:10px;color:var(--navy)}

.main-nav{position:absolute;left:0;top:127px;width:1003px;height:37px;
  background:linear-gradient(var(--nav-top),var(--nav-bottom));border-top:1px solid #3b6392}
.main-nav ul{list-style:none;display:flex;position:absolute;left:133px;top:10px}
.main-nav li{font-size:12.5px;color:var(--white);padding:0 8px;border-left:1px solid #2f5a88;line-height:16px}
.main-nav li:first-child{border-left:0}
.main-nav li.active{color:var(--orange-light)}

.hero{position:absolute;left:0;top:164px;width:1003px;height:329px;background:var(--band);
  border-bottom:1px solid #cfcfcf}
.hero-frame{position:absolute;left:142px;top:27px;width:719px;height:267px;background:var(--white);
  border:1px solid #c9c9c9;padding:4px;box-shadow:0 12px 10px -8px rgba(0,0,0,.35)}
.hero-photo{width:100%;height:100%;background:linear-gradient(90deg,#b9c4cf,#dfe4ea 40%,#c5ccd5 70%,#e6e9ec)}
.hero-arrow{position:absolute;top:144px;width:29px;height:29px;display:flex;align-items:center;justify-content:center}
.hero-arrow.prev{left:100px;background:#a7a7a7}
.hero-arrow.next{left:873px;background:var(--orange)}

.services{position:absolute;left:0;top:494px;width:1003px;height:331px;
  background:linear-gradient(var(--light),#fafafa 50%,#ececec)}
.service{position:absolute;top:43px;width:217px}
.service-photo{width:217px;height:100px}
.service h2{font-family:"Source Sans 3",sans-serif;font-weight:600;font-size:17.5px;color:var(--heading);margin-top:13px}
.service p{font-size:10.8px;line-height:14px;margin-top:13px;height:70px}
.btn{display:inline-block;margin-top:9px;width:100px;height:22px;line-height:22px;border-radius:11px;text-align:center;
  font-size:11px;color:var(--white);background:linear-gradient(var(--orange-light),var(--orange));
  box-shadow:1px 2px 2px rgba(0,0,0,.3)}

.info{position:absolute;left:0;top:825px;width:1003px;height:303px;background:var(--navy-deep);color:var(--white)}
.info-col{position:absolute;top:40px}
.info h3{font-family:"Source Sans 3",sans-serif;font-weight:600;font-size:17.5px;display:flex;align-items:center;gap:6px}
.pager{display:inline-flex;gap:1px}
.pager span{width:11px;height:11px;background:var(--orange);display:flex;align-items:center;justify-content:center}
.case-photo{width:217px;height:100px;margin-top:12px;background:linear-gradient(120deg,#8a9aa8,#dce3ea 60%,#f2f4f6)}
.info p{font-size:11px;line-height:14px}
.more{display:inline-block;font-size:11px;color:var(--orange);text-decoration:underline}
.more::after{content:"›";display:inline-block;margin-left:8px}
.quote{position:absolute;left:30px;top:33px;width:177px;font-style:italic}
.quote-mark{position:absolute;font-family:"Source Sans 3",sans-serif;font-size:52px;color:#44607d;line-height:1}
.news-rule{border-top:1px dashed #3f5d7d;margin-top:8px;width:220px}
.news-title{font-size:12px;margin-top:13px}
.news-date{font-size:10px!important;margin-top:1px}

.site-footer{position:absolute;left:0;top:1128px;width:1003px;height:72px;background:linear-gradient(#eaeaea,#f4f4f4)}
.footer-links{position:absolute;left:141px;top:23px;font-size:10.5px;color:var(--orange)}
.footer-links span{margin:0 4px}
.copyright{position:absolute;left:141px;top:37px;font-size:9px;color:#666}
.social{position:absolute;left:736px;top:21px;display:flex;gap:6px;list-style:none}
.social li{width:27px;height:27px;border-radius:50%;background:var(--nav-top)}
</style>
</head>
<body>

<header class="site-header">
  <div class="brand"><span class="brand-name">KELBROOK <span class="brand-mark"></span></span></div>
  <div class="brand-url">www.kelbrook.com.au</div>
</header>

<nav class="main-nav">
  <ul>
    <li class="active">Home</li>
    <li>Services</li>
    <li>Case studies</li>
    <li>Engaging us</li>
    <li>About Conflict &amp; low performance</li>
    <li>Conflict resolution App</li>
    <li>About</li>
    <li>Contact</li>
  </ul>
</nav>

<section class="hero">
  <a class="hero-arrow prev" aria-label="Previous slide"><svg width="10" height="12" viewBox="0 0 10 12"><path d="M7 1 2 6l5 5" stroke="#fff" stroke-width="2.4" fill="none"/></svg></a>
  <div class="hero-frame"><div class="hero-photo" role="img" aria-label="Photo of a team of five smiling business consultants in front of office buildings"></div></div>
  <a class="hero-arrow next" aria-label="Next slide"><svg width="10" height="12" viewBox="0 0 10 12"><path d="M3 1l5 5-5 5" stroke="#fff" stroke-width="2.4" fill="none"/></svg></a>
</section>

<section class="services">
  <article class="service" style="left:142px">
    <div class="service-photo" role="img" aria-label="Photo of a woman working at a computer in an office" style="background:linear-gradient(90deg,#5c5f55,#a8a49a 50%,#3c4656)"></div>
    <h2>Conflict Management</h2>
    <p>Lorem ipsum dolor sit amet, consectetur adipiscing elit. Etiam eget metus aliquet, egestas erat id, dictum lacus. Sed nisl mauris, tincidunt at faucibus eget, varius et tellus.</p>
    <a class="btn">read more &nbsp;›</a>
  </article>
  <article class="service" style="left:393px">
    <div class="service-photo" role="img" aria-label="Photo of financial charts with a pen" style="background:linear-gradient(135deg,#2f6fb0,#9cc6ea 55%,#d7e9f7)"></div>
    <h2>Performance Management</h2>
    <p>Sed nisi libero, bibendum in commodo eget, venenatis id leo. Praesent condimentum, metus a tempus dapibus, augue lorem blandit lacus, id feugiat libero felis non orci.</p>
    <a class="btn">read more &nbsp;›</a>
  </article>
  <article class="service" style="left:644px">
    <div class="service-photo" role="img" aria-label="Photo of colleagues talking at a meeting table" style="background:linear-gradient(90deg,#b8b0a2,#d9d2c6 45%,#6f6c68)"></div>
    <h2>Change Management</h2>
    <p>Vestibulum ligula metus, convallis sit amet nunc at, malesuada eleifend sem. Nulla vel ultricies quam. Duis sagittis nisi metus, a ullamcorper ante venenatis ac. Nulla tincidunt mi vel ipsum consequat, id ultricies.</p>
    <a class="btn">read more &nbsp;›</a>
  </article>
</section>

<section class="info">
  <div class="info-col" style="left:142px;width:217px">
    <h3>Case Study <span class="pager"><span><svg width="5" height="7" viewBox="0 0 5 7"><path d="M4 0.5 1 3.5l3 3" stroke="#fff" fill="none"/></svg></span><span><svg width="5" height="7" viewBox="0 0 5 7"><path d="M1 0.5l3 3-3 3" stroke="#fff" fill="none"/></svg></span></span></h3>
    <div class="case-photo" role="img" aria-label="Photo of two colleagues reviewing documents together"></div>
    <p style="margin-top:21px">Praesent suscipit lobortis blandit. Duis rutrum leo a arcu vestibulum, vel consequat libero interdum.</p>
    <a class="more" style="margin-top:16px">view more case studies</a>
  </div>

  <div class="info-col" style="left:393px;width:220px;height:230px">
    <h3>Customer Testimonials</h3>
    <span class="quote-mark" style="left:0;top:24px">“</span>
    <div class="quote">
      <p>Suspendisse lobortis lacinia feugiat. Integer nec nulla dui. Quisque a justo at arcu laoreet sagittis. Donec placerat lectus id dolor interdum porttitor. Vivamus in erat bibendum, luctus justo ut, condimentum nulla. Vestibulum ante ipsum primis in faucibus orci luctus et ultrices.</p>
      <p style="font-style:normal;margin-top:14px">~Anonymous, AU</p>
      <a class="more" style="font-style:normal;margin-top:16px">view all testimonials</a>
    </div>
    <span class="quote-mark" style="left:195px;top:168px">”</span>
  </div>

  <div class="info-col" style="left:644px;width:230px">
    <h3>News &amp; Updates</h3>
    <div class="news-rule"></div>
    <p class="news-title">Praesent suscipit lobortis blandit.</p>
    <p class="news-date">Sept 19 2013</p>
    <a class="more" style="margin-top:11px">view all news</a>
    <h3 style="margin-top:22px">Contact Information</h3>
    <p style="margin-top:9px;font-size:11.5px"><b>Address:</b><br>Building No Street Name City Australia</p>
    <p style="margin-top:13px;font-size:11.5px"><b>Email Address:</b> <span style="text-decoration:underline">info@kelbrook.com.au</span><br><b>Phone Number:</b> 1234 567 890</p>
  </div>
</section>

<footer class="site-footer">
  <div class="footer-links">Home<span>|</span>Terms of Use<span>|</span>Sitemap</div>
  <div class="copyright">Copyright © 2013 Kelbrook. All rights reserved.</div>
  <ul class="social" aria-label="Social links">
    <li aria-label="Social link 1"></li>
    <li aria-label="Social link 2"></li>
    <li aria-label="Social link 3"></li>
    <li aria-label="Social link 4"></li>
  </ul>
</footer>

</body>
</html>
```